Building and constructions

Extension, additions, alterations, renovations, new homes, project management and supervision

Industry/Entity Type

Building

Contact Information for Business Card

Morlaven building service constructions PTY LTD
Colin Marsh builder/ supervisor
BLD 71940 member of HTU
0411273509 email cmarsh71@qelmoranet.com

```html
<!DOCTYPE html>
<html lang="en">
<head>
<meta charset="utf-8">
<title>Morlaven Building Service Constructions – Business Cards</title>
<link href="https://fonts.googleapis.com/css2?family=Saira+Semi+Condensed:wght@600&display=swap" rel="stylesheet">
<style>
  :root {
    --teal: #2d8fb4;
    --teal-deep: #1c6a86;
    --teal-frame: #2a7d9c;
    --paper: #ffffff;
    --bg: #ffffff;
  }
  * { box-sizing: border-box; margin: 0; padding: 0; }
  html, body { width: 1200px; height: 923px; overflow: hidden; background: var(--bg); }
  body { font-family: "Saira Semi Condensed", "Arial Narrow", sans-serif; font-weight: 600; position: relative; }

  .frame-right { position: absolute; left: 1168px; top: 0; width: 9px; height: 923px; background: var(--teal-frame); }
  .frame-bottom { position: absolute; left: 0; top: 886px; width: 1200px; height: 6px; background: var(--teal-frame); }

  .brand-lockup { position: absolute; left: 22px; top: 30px; width: 330px; color: var(--teal); }
  .brand-lockup .brand-mark { display: inline-block; width: 26px; height: 26px; background: var(--teal); margin-bottom: 10px; }
  .brand-lockup .brand-name { font-size: 76px; line-height: 1; letter-spacing: 2px; text-transform: uppercase; }
  .brand-lockup .brand-line { font-size: 17px; letter-spacing: 0.2px; text-transform: uppercase; margin-top: 8px; }

  .card { position: absolute; width: 480px; height: 275px; box-shadow: 0 8px 22px rgba(0,0,0,0.18); overflow: hidden; }

  /* front */
  .card-front { left: 120px; top: 440px; background: var(--paper); }
  .card-front .info-band { position: absolute; left: 0; right: 0; top: 118px; bottom: 0; background: var(--teal); }
  .card-front .info-rule { position: absolute; left: 0; right: 0; top: 232px; height: 4px; background: var(--paper); }
  .card-front .card-brand { position: absolute; right: 30px; top: 24px; text-align: right; color: var(--teal); text-transform: uppercase; }
  .card-front .card-brand .card-brand-name { font-size: 36px; line-height: 1; letter-spacing: 1px; }
  .card-front .card-brand .card-brand-line { font-size: 9px; margin-top: 4px; }
  .card-front .holder { position: absolute; right: 30px; top: 126px; text-align: right; color: var(--paper); text-transform: uppercase; }
  .card-front .holder-name { font-size: 22px; letter-spacing: 1px; }
  .card-front .holder-role, .card-front .holder-licence { font-size: 14px; letter-spacing: 0.5px; margin-top: 4px; }
  .card-front .contact-line { position: absolute; left: 22px; right: 22px; top: 244px; color: var(--paper); font-size: 14px; letter-spacing: 0.4px; text-transform: uppercase; white-space: nowrap; }

  /* back */
  .card-back { left: 650px; top: 230px; background: var(--teal); }
  .card-back .edge-band { position: absolute; left: 0; top: 0; bottom: 0; width: 22px; background: var(--teal-deep); border-right: 4px solid var(--paper); }
  .card-back .foot-band { position: absolute; left: 0; right: 0; bottom: 0; height: 30px; background: var(--teal-deep); border-top: 4px solid var(--paper); }
  .card-back .brand-plate { position: absolute; left: 110px; top: 60px; width: 270px; height: 118px; background: var(--paper);
    display: flex; flex-direction: column; align-items: center; justify-content: center; color: var(--teal); text-transform: uppercase; }
  .card-back .brand-plate .plate-name { font-size: 40px; line-height: 1; letter-spacing: 1px; }
  .card-back .brand-plate .plate-line { font-size: 10px; margin-top: 6px; }
</style>
</head>
<body>
  <div class="frame-right"></div>
  <div class="frame-bottom"></div>

  <header class="brand-lockup">
    <span class="brand-mark"></span>
    <div class="brand-name">Morlaven</div>
    <div class="brand-line">Building service constructions PTY LTD</div>
  </header>

  <section class="card card-back" aria-label="Business card back">
    <div class="edge-band"></div>
    <div class="brand-plate">
      <div class="plate-name">Morlaven</div>
      <div class="plate-line">Building service constructions PTY LTD</div>
    </div>
    <div class="foot-band"></div>
  </section>

  <section class="card card-front" aria-label="Business card front">
    <div class="card-brand">
      <div class="card-brand-name">Morlaven</div>
      <div class="card-brand-line">Building service constructions PTY LTD</div>
    </div>
    <div class="info-band"></div>
    <div class="holder">
      <div class="holder-name">Colin Marsh</div>
      <div class="holder-role">Builder/Supervisor</div>
      <div class="holder-licence">BLD 71940 Member of HTU</div>
    </div>
    <div class="info-rule"></div>
    <div class="contact-line">Phone-0411273509 &nbsp; Email-cmarsh71@qelmoranet.com</div>
  </section>
</body>
</html>
```